Korvel Professional Services Website

Small website for company presence and information. Company is an IT/Telecom services company. We provide presales and installation services. Included are various company logos including color levels. Site doesn't have to use these exact colors in the logos, but should be complimentary if using different colors. It should have a professional business appearance.
Updates

My apologies for not being more responsive on the designs that have been submitted. I will be narrowing down the submissions and providing additional feedback next week. Thank you for your patience.

Project Deadline Extended
Reason: Sorry again for delays on picking designs. Work has me very busy and I've just not had the time to devote to this project. I am extending the design deadline for a few more days to give me time to make my final decisions. Thank you all for your patience. Stay tuned....

Target Market(s)

Telecom sales companies that sell Quenti telecom products.

Industry/Entity Type

Professional Service

Coding

Coded - Design and coding required

Number of Pages Required

5+ page

Font styles to use
Sans Serif

Colors
3276b5
0355a3
85abd2
85cae6
33a6d7
0692cd
ffffff

Requirements
Must have
• Professional design reflective of IT/Telecom business. A good reference website would be: http://www.lorbextech.example/. Looking for something similar in function and presence.
Nice to have
• Rolling photos highlighting our services. Traditional navigation across the top of all pages.
Should not have
• No motion video, flashy presentation or overly confused interface.

```html
<!DOCTYPE html>
<html lang="en">
<head>
<meta charset="utf-8">
<title>Korvel Professional Services</title>
<link href="https://fonts.googleapis.com/css2?family=Roboto:ital,wght@0,400;0,500;0,700;1,400&family=Reenie+Beanie&display=swap" rel="stylesheet">
<style>
:root{
  --navy:#1f4e93;
  --blue:#3276b5;
  --bright:#0b6cc4;
  --sky:#85cae6;
  --ink:#1d1d1d;
  --text:#555;
  --pale:#f2f4f7;
  --rule:#3f8fd6;
  --white:#fff;
}
*{box-sizing:border-box;margin:0;padding:0}
html,body{width:718px;height:1200px;overflow:hidden;background:var(--white);font-family:"Roboto",Arial,sans-serif;color:var(--ink)}
.page{position:relative;width:718px;height:1200px}
.abs{position:absolute}
.topbar{top:0;left:0;width:718px;height:19px;font-size:7.5px;color:#666}
.topbar .contact{position:absolute;right:110px;top:5px;display:flex;gap:18px}
.topbar .social{position:absolute;right:35px;top:4px;display:flex;gap:6px}
.sq{width:11px;height:11px;border-radius:2px;display:inline-block}
.sq.a{background:#3b5998}.sq.b{background:#33a6d7}.sq.c{background:#d9453b}
.navband{top:19px;left:0;width:718px;height:42px;background:linear-gradient(90deg,var(--navy),var(--blue))}
.nav{position:absolute;right:30px;top:15px;display:flex;gap:23px;font-size:9px;font-weight:700;color:var(--white)}
.logo{top:19px;left:30px;width:152px;height:51px;background:var(--white);border-radius:0 0 5px 5px;display:flex;align-items:center;justify-content:center;gap:6px;z-index:3}
.logo .mark{width:14px;height:14px;border-radius:50%;background:var(--navy)}
.logo .name{font-size:11px;font-weight:700;color:var(--navy);line-height:1.1}
.hero{top:61px;left:0;width:718px;height:293px;background:linear-gradient(160deg,#4ea7dd 0%,#3d8fcf 45%,#2f7ec2 100%)}
.hero h1{position:absolute;top:85px;width:100%;text-align:center;font-family:"Reenie Beanie",cursive;font-weight:400;font-size:34px;line-height:31px;color:var(--white)}
.hero .sub{position:absolute;top:155px;width:100%;text-align:center;font-size:10px;font-weight:500;color:var(--white);letter-spacing:.3px}
.hero .btn{position:absolute;top:179px;left:328px;width:61px;height:20px;background:var(--white);border-radius:2px;font-size:6px;font-weight:700;display:flex;align-items:center;justify-content:center}
.hero svg{position:absolute;left:0;top:220px}
.title{position:absolute;left:0;width:718px;text-align:center;font-size:13.5px;font-weight:500}
.title span{color:var(--bright)}
.dots{position:absolute;left:31px;width:656px;border-top:1px dashed var(--rule)}
.welcome-copy{top:391px;left:32px;width:654px;text-align:center;font-size:7.2px;line-height:12px;color:#333}
.services{top:417px;left:0;width:718px;height:207px;background:var(--pale)}
.tabs{position:absolute;top:8px;left:269px;display:flex;gap:16px;align-items:center}
.tab{font-size:11px;font-weight:500;padding:7px 10px}
.tab.on{border:1px solid var(--bright);color:var(--bright);border-radius:2px;background:var(--white)}
.svc{position:absolute;top:61px;width:110px;margin-left:-55px;text-align:center;font-size:11px;font-weight:700;line-height:14px}
.svc .photo{width:84px;height:84px;border-radius:50%;margin:0 auto 10px}
.mail{top:624px;left:0;width:718px;height:53px;background:linear-gradient(90deg,var(--navy),var(--blue))}
.mail .lbl{position:absolute;left:67px;top:15px;font-size:7.5px;font-weight:500;color:var(--white);line-height:12px}
.mail .field{position:absolute;top:17px;width:151px;height:19px;background:var(--white);border-radius:2px;font-size:7px;color:#999;padding:5px 8px}
.mail .submit{position:absolute;top:17px;left:631px;width:56px;height:19px;background:var(--white);border-radius:2px;font-size:7.5px;font-weight:700;text-align:center;line-height:19px}
.card{position:absolute;top:722px;width:152px;height:212px;background:#f4f5f7}
.card .photo{height:114px}
.card h3{font-size:11px;font-weight:500;margin:9px 11px 6px}
.card p{font-size:7.3px;line-height:12px;color:var(--text);margin:0 11px;height:38px}
.card .meta{position:absolute;bottom:10px;left:11px;right:11px;border-top:1px dashed #ccc;padding-top:8px;font-size:6.5px;color:#666;display:flex;justify-content:space-between}
.quotes{top:950px;left:0;width:718px;height:126px;background:var(--pale)}
.quote{position:absolute;top:62px;width:250px;font-size:7.3px;line-height:12px;font-style:italic;color:#555}
.quote b{display:block;font-style:normal;font-weight:500;color:var(--ink);margin-top:6px}
.avatar{position:absolute;top:58px;width:46px;height:46px;border-radius:50%;background:linear-gradient(#c9b8a8,#8d7766)}
.likebar{top:1084px;left:225px;width:268px;height:28px;border:1px solid #e2e2e2;border-radius:14px;background:var(--white);font-size:6px;display:flex;align-items:center;padding-left:72px;gap:4px}
.likebtn{background:#4267b2;color:var(--white);font-weight:700;padding:2px 4px;border-radius:2px}
.footer{top:1119px;left:0;width:718px;height:81px;border-top:2px solid var(--blue)}
.fnav{position:absolute;top:33px;left:36px;display:flex;gap:17px;font-size:7.5px;font-weight:500}
.flinks{position:absolute;top:57px;left:37px;display:flex;gap:13px;font-size:6.5px;color:#444}
.flogo{position:absolute;top:18px;right:36px;display:flex;align-items:center;gap:6px;font-size:10px;font-weight:700;color:var(--navy)}
.fcopy{position:absolute;top:56px;right:36px;display:flex;gap:8px;align-items:center;font-size:6.5px;color:#444}
.fline{position:absolute;top:49px;left:36px;width:646px;border-top:1px dashed #ccc}
</style>
</head>
<body>
<div class="page">
  <div class="abs topbar">
    <div class="contact"><span>&#9742; +1 800 555 01 47</span><span>&#9993; info@korvelservices.example</span></div>
    <div class="social"><i class="sq a"></i><i class="sq b"></i><i class="sq c"></i></div>
  </div>
  <div class="abs navband">
    <nav class="nav"><span>HOME</span><span>ABOUT</span><span>SERVICES</span><span>SOLUTIONS</span><span>BLOG</span><span>CONTACT</span></nav>
  </div>
  <div class="abs logo"><i class="mark"></i><div class="name">KORVEL<br><span style="font-size:6px">PROFESSIONAL SERVICES</span></div></div>

  <section class="abs hero" role="img" aria-label="Blue-tinted photo of people working at laptops in an office">
    <h1>The costs of doing<br>nothing are very real.</h1>
    <p class="sub">But so are the costs of doing the wrong something.</p>
    <div class="btn">REGISTER NOW</div>
    <svg width="718" height="73" viewBox="0 0 718 73" fill="none" stroke="rgba(255,255,255,.5)" stroke-width="1">
      <polyline points="0,36 24,29 48,27 72,34 96,32 110,43 130,17 150,34 170,30 184,40 204,36 220,34 234,14 250,42 268,52 290,44 310,52 330,48 350,42 372,50 392,46 412,36 430,44 452,26 462,30 480,14 500,28 520,32 540,30 564,32 584,14 604,26 630,32 648,30 668,40 684,24 700,34 718,38"/>
      <g fill="rgba(255,255,255,.35)"><circle cx="130" cy="17" r="3"/><circle cx="234" cy="14" r="3"/><circle cx="412" cy="36" r="3"/><circle cx="480" cy="14" r="3"/><circle cx="584" cy="14" r="3"/><circle cx="684" cy="24" r="3"/></g>
    </svg>
  </section>

  <h2 class="title" style="top:356px">Welcome to <span>Korvel Professional Services</span></h2>
  <div class="dots" style="top:378px"></div>
  <p class="abs welcome-copy">Sed ut perspiciatis unde omnis iste natus error sit voluptatem accusantium doloremque laudantium, totam rem aperiam, eaque ipsa quae ab illo inventore veritatis et quasi architecto beatae vitae dicta sunt explicabo. Sed ut perspiciatis unde omnis iste natus error sit voluptatem accusantium doloremque laudantium.</p>

  <section class="abs services">
    <div class="tabs"><span class="tab on">Our Service</span><span class="tab">Our Solutions</span></div>
    <div class="dots" style="top:44px;left:39px;width:640px"></div>
    <div class="svc" style="left:78px"><div class="photo" role="img" aria-label="City skyline photo with a bank icon" style="background:linear-gradient(#9aa3ad,#4d5560)"></div>Banking Financial Services</div>
    <div class="svc" style="left:189px"><div class="photo" role="img" aria-label="Photo of medical staff with a first aid icon" style="background:linear-gradient(#e7e9ec,#b9c3cc)"></div>Healthcare</div>
    <div class="svc" style="left:298px"><div class="photo" role="img" aria-label="Photo of a business meeting with a shield icon" style="background:linear-gradient(#dfe2e5,#a9b1b8)"></div>Life &amp; Annyuity Insurance</div>
    <div class="svc" style="left:408px"><div class="photo" role="img" aria-label="Photo of a delivery truck with a cart icon" style="background:linear-gradient(#b7b9bc,#5c5f63)"></div>Transportation Logistics</div>
    <div class="svc" style="left:518px"><div class="photo" role="img" aria-label="Beach photo with a plane icon" style="background:linear-gradient(#5ab6e6,#d9cfb8)"></div>Travel Leisure</div>
    <div class="svc" style="left:628px"><div class="photo" role="img" aria-label="Power lines at dusk with a flame icon" style="background:linear-gradient(#2f4b8c,#c77a3a)"></div>Utilities</div>
  </section>

  <section class="abs mail">
    <svg class="abs" style="left:30px;top:18px" width="22" height="18" viewBox="0 0 22 18" fill="none" stroke="#fff" stroke-width="1.6"><path d="M3 2h11a2 2 0 0 1 2 2v5a2 2 0 0 1-2 2H8l-4 3v-3H3a2 2 0 0 1-2-2V4a2 2 0 0 1 2-2z"/><path d="M18 6h1a2 2 0 0 1 2 2v4a2 2 0 0 1-2 2h-1v3l-4-3"/></svg>
    <div class="lbl">Feel Free<br>to Mail</div>
    <div class="field" style="left:143px">Full Name *</div>
    <div class="field" style="left:306px">Phone Number *</div>
    <div class="field" style="left:468px">Your Email *</div>
    <div class="submit">SUBMIT</div>
  </section>

  <h2 class="title" style="top:683px">Latest <span>Blog &amp; Views</span></h2>
  <div class="dots" style="top:705px"></div>

  <article class="card" style="left:31px"><div class="photo" role="img" aria-label="Photo of a traveller with a bag walking through a doorway" style="background:linear-gradient(#6c5a4c,#3a2e28)"></div><h3>Standard Post</h3><p>Enim congue blandit. Lorem ipsum dolor sit amet, consectetur adipiscing elit. Quisque...</p><div class="meta"><span>&#9638; 22 June, 2015</span><span>&#9679; 0</span></div></article>
  <article class="card" style="left:199px"><div class="photo" role="img" aria-label="Photo of a coffee carafe on a table" style="background:linear-gradient(#9a9a94,#6d6a64)"></div><h3>Video Post</h3><p>Ultrices posuere cubilia curae curabitur sit amet tortor ut massa commodo. Vestibulum...</p><div class="meta"><span>&#9638; 22 June, 2015</span><span>&#9679; 0</span></div></article>
  <article class="card" style="left:367px"><div class="photo" role="img" aria-label="Photo of a cafe table against a brick wall" style="background:linear-gradient(#7c5a44,#3e2d24)"></div><h3>Post with Image</h3><p>Enim congue blandit. Lorem ipsum dolor sit amet, consectetur adipiscing elit. Quisque...</p><div class="meta"><span>&#9638; 22 June, 2015</span><span>&#9679; 0</span></div></article>
  <article class="card" style="left:535px"><div class="photo" role="img" aria-label="Photo of a leather wallet on a table" style="background:linear-gradient(#b5a58f,#6e5a46)"></div><h3>Image Post</h3><p>Ultrices posuere cubilia curae curabitur sit amet tortor ut massa commodo. Vestibulum...</p><div class="meta"><span>&#9638; 22 June, 2015</span><span>&#9679; 3</span></div></article>

  <section class="abs quotes">
    <h2 class="title" style="top:10px">What <span>People Say</span></h2>
    <div class="dots" style="top:32px"></div>
    <div class="quote" style="left:26px;text-align:right">Duis aute irure dolor in reprehenderit in voluptate velit esse cillum dolore eu fugiat nulla pariatur. Excepteur sint occaecat cupidatat non proident, sunt in culpa qui officia deserunt mollit.<b>Marcus Hale, Operations Manager</b></div>
    <div class="avatar" role="img" aria-label="Portrait photo of the reviewer" style="left:294px"></div>
    <div class="abs" style="left:358px;top:60px;height:50px;border-left:1px dashed var(--rule)"></div>
    <div class="avatar" role="img" aria-label="Portrait photo of the reviewer" style="left:378px"></div>
    <div class="quote" style="left:442px">Provident, similique sunt in culpa qui officia deserunt mollitia animi, id est laborum et dolorum fuga. Et harum quidem rerum facilis est et expedita distinctio. Nam libero tempore, cum soluta nobis.<b>Nora Bexley, Creative Designer</b></div>
  </section>

  <div class="abs" style="top:1098px;left:38px;width:640px;border-top:1px solid #e6e6e6;z-index:0"></div>
  <div class="abs likebar"><span class="likebtn">&#10003; Like</span><span>You and 4k others like this.</span></div>

  <footer class="abs footer">
    <div class="fnav"><span>&#9906;</span><span>Help &amp; Contact</span><span>Services</span><span>Solutions</span><span>Events</span></div>
    <div class="flogo"><i class="sq" style="background:var(--navy);border-radius:50%;width:14px;height:14px"></i>KORVEL</div>
    <div class="fline"></div>
    <div class="flinks"><span>About</span><span>Blog</span><span>Jobs</span><span>Careers</span><span>Public Policy</span><span>Sitemap</span><span>Global Support</span><span>Partners</span></div>
    <div class="fcopy"><span>© 2015–2017</span><span>Privacy</span><i class="sq a"></i><i class="sq b"></i><i class="sq c"></i></div>
  </footer>
</div>
</body>
</html>
```